One Page Template Mobile Reviews

Move our reviews web site template to a mobile template.
We produce a review web site for our customers like this one:

http://dental.quillorbit.com/surveys47615/KoP31RTM/surveys.htm

These are X pages with the exact same format.
We need to have this format adapted to an iPhone format.

So this is really ONE page project!

Target Market(s)

Patients looking for feedback on a particular practice

Industry/Entity Type

Dental

Requirements
Must have
• Running on iPhone using the HTML "viewport" tags

```html
<!DOCTYPE html>
<html lang="en">
<head>
<meta charset="utf-8">
<meta name="viewport" content="width=device-width, initial-scale=1">
<title>QuillOrbit – Patient Reviews</title>
<link rel="stylesheet" href="https://fonts.googleapis.com/css2?family=PT+Sans:ital,wght@0,400;0,700;1,400&family=Open+Sans:ital,wght@0,400;0,600;0,700;1,400&display=swap">
<style>
  :root{
    --page-bg:#ececec;
    --header-top:#f2f2f2;
    --header-bottom:#ffffff;
    --brand:#7a1f2b;
    --phone-label:#8a8a8a;
    --phone-number:#8b1d1d;
    --tagline:#555555;
    --doctor-name:#4f8a10;
    --score:#a01c1c;
    --muted:#6b6b6b;
    --link:#3b3bc4;
    --section-title:#4b4bcf;
    --panel-bg:#e6e6e6;
    --box-border:#cfcfcf;
    --band:#5f9ea0;
    --star:#f5c400;
    --star-edge:#c99a00;
    --scroll-track:#d4d4d4;
    --scroll-thumb:#9a2323;
    --photo:#7d8a99;
    --map:#e9e4da;
    --avatar:#d9c9b4;
    --review-title:#a01c1c;
    --text:#333333;
  }
  *{box-sizing:border-box;margin:0;padding:0}
  html,body{width:1200px;height:1080px;overflow:hidden;background:var(--page-bg)}
  body{position:relative;font-family:"Open Sans",sans-serif;color:var(--text)}

  .screen{
    position:absolute;left:8px;top:192px;width:845px;height:497px;
    transform:scale(1.4);transform-origin:0 0;
    background:var(--panel-bg);overflow:hidden;
  }

  /* header */
  .site-header{
    position:absolute;left:0;top:0;width:826px;height:78px;
    background:linear-gradient(var(--header-top),var(--header-bottom));
    border-bottom:1px solid #dcdcdc;
  }
  .brand{
    position:absolute;left:18px;top:24px;
    font-family:"PT Sans",sans-serif;font-size:34px;font-weight:400;color:var(--brand);
    display:flex;align-items:center;gap:8px;line-height:1;
  }
  .brand-dot{width:12px;height:12px;border-radius:50%;background:var(--brand)}
  .contact-phone{
    position:absolute;right:32px;top:10px;
    font-family:"PT Sans",sans-serif;font-style:italic;font-size:17px;color:var(--phone-label);
  }
  .contact-phone strong{color:var(--phone-number);font-weight:400}
  .tagline{
    position:absolute;right:33px;top:41px;
    font-family:"PT Sans",sans-serif;font-size:17.5px;color:var(--tagline);letter-spacing:.2px;
  }

  /* scrollbar */
  .scroll-track{position:absolute;left:826px;top:78px;width:19px;height:419px;background:var(--scroll-track)}
  .scroll-thumb{position:absolute;left:4px;top:4px;width:10px;height:100px;border-radius:5px;background:var(--scroll-thumb)}

  /* profile */
  .profile{position:absolute;left:0;top:78px;width:826px;height:104px;background:#fff}
  .profile-photo{position:absolute;left:16px;top:9px;width:80px;height:82px;background:linear-gradient(160deg,#c9d6e4,var(--photo));border:1px solid #bbb}
  .doctor-name{
    position:absolute;left:109px;top:5px;display:flex;align-items:center;gap:10px;
    font-family:"PT Sans",sans-serif;font-size:15.5px;font-weight:700;color:var(--doctor-name);
  }
  .rating-line{position:absolute;left:108px;top:28px;font-size:12px;color:var(--muted);letter-spacing:.3px}
  .rating-line .score{color:var(--score);font-weight:700;margin-right:8px}
  .site-link{position:absolute;left:105px;top:44px;font-size:11.5px;color:var(--link);text-decoration:none;letter-spacing:.3px}
  .address{position:absolute;left:105px;top:70px;font-size:10px;font-style:italic;line-height:12.5px;color:#444}
  .page-count{position:absolute;right:15px;top:9px;font-size:12.5px;color:#222}

  .stars{display:flex;gap:2px}
  .stars svg{width:22px;height:21px}

  /* panels */
  .box{position:absolute;background:#fff;border:1px solid var(--box-border)}
  .box-title{
    display:block;text-align:center;margin-top:8px;
    font-family:"PT Sans",sans-serif;font-size:15.5px;color:var(--section-title);letter-spacing:.3px;
  }
  .hours{left:15px;top:190px;width:220px;height:137px}
  .hours-table{position:absolute;left:10px;top:40px;width:200px;border-collapse:collapse;font-size:12px;color:#333}
  .hours-table td{height:22.3px;padding:0}
  .hours-table td:last-child{text-align:right;white-space:nowrap}
  .location{left:249px;top:190px;width:561px;height:176px}
  .map-area{position:absolute;left:0;top:31px;width:559px;height:143px;background:linear-gradient(120deg,#efece4,var(--map) 60%,#dfe9cf)}

  .review-band{
    position:absolute;left:15px;top:378px;width:795px;height:29px;background:var(--band);
    color:#fff;font-family:"PT Sans",sans-serif;font-size:15.5px;line-height:29px;padding-left:11px;letter-spacing:.3px;
  }
  .band-note{position:absolute;left:14px;top:414px;font-size:10.5px;color:#333;letter-spacing:.2px}

  .review-card{position:absolute;left:15px;top:437px;width:795px;height:70px;background:#fff;border:1px solid #ddd}
  .reviewer-avatar{position:absolute;left:14px;top:11px;width:80px;height:70px;background:linear-gradient(#f3efe9,var(--avatar));border:1px solid #ccc}
  .review-rating{position:absolute;left:102px;top:12px;display:flex;align-items:center;gap:6px;font-size:12px;color:var(--muted);letter-spacing:.3px}
  .review-rating .stars svg{width:19px;height:18px}
  .expand-toggle{width:13px;height:11px;border:1px solid #9ab;background:#e8eef5;display:inline-flex;align-items:center;justify-content:center}
  .review-title{position:absolute;left:105px;top:37px;font-size:12px;font-weight:700;color:var(--review-title);letter-spacing:.3px}
  .review-index{position:absolute;right:10px;top:9px;font-size:10.5px;color:#555}
  .review-index b{color:#111}
</style>
</head>
<body>
<svg width="0" height="0" style="position:absolute" aria-hidden="true">
  <defs>
    <symbol id="star" viewBox="0 0 24 23">
      <polygon points="12,1 15,8.4 23,8.9 16.9,14 18.8,22 12,17.6 5.2,22 7.1,14 1,8.9 9,8.4" fill="var(--star)" stroke="var(--star-edge)" stroke-width="1"/>
    </symbol>
    <symbol id="star-half" viewBox="0 0 24 23">
      <clipPath id="left-half"><rect x="0" y="0" width="12" height="23"/></clipPath>
      <polygon points="12,1 15,8.4 23,8.9 16.9,14 18.8,22 12,17.6 5.2,22 7.1,14 1,8.9 9,8.4" fill="none" stroke="var(--star-edge)" stroke-width="1.2"/>
      <polygon clip-path="url(#left-half)" points="12,1 15,8.4 23,8.9 16.9,14 18.8,22 12,17.6 5.2,22 7.1,14 1,8.9 9,8.4" fill="var(--star)" stroke="var(--star-edge)" stroke-width="1"/>
    </symbol>
  </defs>
</svg>

<main class="screen">
  <header class="site-header">
    <div class="brand"><span class="brand-dot"></span>QuillOrbit</div>
    <p class="contact-phone">Phone: <strong>(555) 014-2750</strong></p>
    <p class="tagline">Reviews From Verified Patients Only</p>
  </header>

  <section class="profile">
    <div class="profile-photo" role="img" aria-label="Portrait photo of the dentist"></div>
    <h1 class="doctor-name">Daniel Marwick DDS, FAGD
      <span class="stars">
        <svg><use href="#star"/></svg><svg><use href="#star"/></svg><svg><use href="#star"/></svg><svg><use href="#star"/></svg><svg><use href="#star-half"/></svg>
      </span>
    </h1>
    <p class="rating-line"><span class="score">98.19 %</span>747 Reviews &amp; Surveys</p>
    <a class="site-link" href="#">www.drmarwick.com</a>
    <p class="address">4120 Birchwood Lane Suite 210<br>Fairhaven, VA 22150</p>
    <p class="page-count">Page 1 / 30</p>
  </section>

  <section class="box hours">
    <span class="box-title">OFFICE HOURS</span>
    <table class="hours-table">
      <tr><td>Monday</td><td>7:30 AM 2:00 PM</td></tr>
      <tr><td>Tuesday</td><td>7:30 AM 5:00 PM</td></tr>
      <tr><td>Wednesday</td><td>7:30 AM 5:00 PM</td></tr>
      <tr><td>Thursday</td><td>7:30 AM 1:00 PM</td></tr>
    </table>
  </section>

  <section class="box location">
    <span class="box-title">OFFICE HOURS</span>
    <div class="map-area" role="img" aria-label="Street map showing the office location with a pin marker"></div>
  </section>

  <h2 class="review-band">747 Certified Patients Reviews &amp; Surveys for Daniel Marwick DDS, FAGD</h2>
  <p class="band-note">Reviews posted and surveys rated from actual patients. Certified</p>

  <article class="review-card">
    <div class="reviewer-avatar" role="img" aria-label="Reviewer profile avatar"></div>
    <div class="review-rating">
      <span class="stars">
        <svg><use href="#star"/></svg><svg><use href="#star"/></svg><svg><use href="#star"/></svg><svg><use href="#star"/></svg><svg><use href="#star-half"/></svg>
      </span>
      100.00 %
      <span class="expand-toggle"><svg width="8" height="5" viewBox="0 0 8 5"><polygon points="0,0 8,0 4,5" fill="#3a6ea5"/></svg></span>
    </div>
    <p class="review-title">I am especially grateful that ...</p>
    <p class="review-index">Review(743): <b>1</b> /747</p>
  </article>

  <div class="scroll-track"><div class="scroll-thumb"></div></div>
</main>
</body>
</html>
```